Modern Innovative Business Card Design

We require a nice, modern, clean business card design, ready for upload to Cardomora. Our company develops online banking software solutions for small financial insitutions. The design should be clean, professional, but yet not "corporate boring". See www.fyrolt.com for an idea of business image and profile. The design should communicate innovation, be modern and fresh, yet look professional and established.

Target Market(s)

Finance industry, bankers, entrepreneurs

Industry/Entity Type

Financial

Contact Information for Business Card

Tobias Wendlerup
CEO

FYROLT BV
Lindenwerf 38
1027 HX Amsterdam
The Netherlands

Phone: +31 20 517 8036
Direct: +31 20 604 1758
Skype: tobias.fyrolt
ceo@fyrolt.com
www.fyrolt.com

Font styles to use
Sans Serif

Requirements
Must have
• Should look clean, modern and professional. File should be ready for upload to cardomora.
Should not have
• Boring standard corporate layout

```html
<!DOCTYPE html>
<html lang="en">
<head>
<meta charset="utf-8">
<title>FYROLT – Business Card</title>
<link rel="stylesheet" href="https://fonts.googleapis.com/css2?family=Ubuntu:wght@400;500&display=swap">
<style>
  :root {
    --page-bg: #e9e7e3;
    --card-white: #ffffff;
    --brand-green: #8cc63f;
    --brand-green-light: #b5db7c;
    --slate: #5b5c5e;
    --ink: #5a5a5c;
    --text-light: #ffffff;
  }
  html, body {
    margin: 0;
    width: 1200px;
    height: 1000px;
    overflow: hidden;
    background: var(--page-bg);
    font-family: "Ubuntu", sans-serif;
  }
  .business-card {
    position: absolute;
    left: 75px;
    top: 200px;
    width: 1050px;
    height: 600px;
    box-shadow: 0 10px 30px rgba(0,0,0,0.18);
  }
  .business-card svg { display: block; }
  .card-white { fill: var(--card-white); }
  .green-band { fill: var(--brand-green); }
  .green-rim { fill: var(--brand-green-light); }
  .slate-disc { fill: var(--slate); }
  .wordmark { font-family: "Ubuntu", sans-serif; font-weight: 500; font-size: 96px; fill: var(--ink); letter-spacing: 2px; }
  .wordmark-square { fill: var(--brand-green); }
  .holder-name { font-family: "Ubuntu", sans-serif; font-weight: 500; font-size: 36px; fill: var(--text-light); }
  .holder-title { font-family: "Ubuntu", sans-serif; font-size: 28px; fill: var(--text-light); }
  .contact-line { font-family: "Ubuntu", sans-serif; font-size: 23px; fill: var(--text-light); }
  .company-name { font-family: "Ubuntu", sans-serif; font-weight: 500; font-size: 25px; fill: var(--brand-green); }
  .icon { fill: none; stroke: var(--brand-green); stroke-width: 2.5; }
  .icon-solid { fill: var(--brand-green); }
</style>
</head>
<body>
  <div class="business-card">
    <svg width="1050" height="600" viewBox="0 0 1050 600" xmlns="http://www.w3.org/2000/svg">
      <defs>
        <clipPath id="card-shape"><rect width="1050" height="600"/></clipPath>
      </defs>
      <g clip-path="url(#card-shape)">
        <rect class="card-white" width="1050" height="600"/>
        <path class="green-band" d="M360 0 H1050 V220 H660 Q470 190 360 0 Z"/>
        <circle class="green-rim" cx="976" cy="700" r="580"/>
        <circle class="green-band" cx="984" cy="700" r="570"/>
        <circle class="slate-disc" cx="990" cy="700" r="560"/>
      </g>

      <text class="wordmark" x="80" y="400">FYROLT</text>
      <rect class="wordmark-square" x="88" y="420" width="28" height="28"/>

      <text class="holder-name" x="1005" y="70" text-anchor="end">Tobias Wendlerup</text>
      <text class="holder-title" x="1005" y="110" text-anchor="end">CEO</text>

      <text class="contact-line" x="935" y="290" text-anchor="end">+31 20 517 8036 (NED)</text>
      <text class="contact-line" x="935" y="326" text-anchor="end">+31 20 604 1758 (Direct)</text>
      <text class="contact-line" x="935" y="362" text-anchor="end">tobias.fyrolt.ceo@fyrolt.com</text>
      <text class="contact-line" x="935" y="398" text-anchor="end">www.fyrolt.com</text>

      <g class="contact-icons">
        <path class="icon" d="M952 276 q2 -6 8 -6 l4 6 -3 3 q3 6 8 9 l3 -3 6 4 q0 6 -6 8 q-12 -2 -20 -21 z"/>
        <rect class="icon" x="988" y="270" width="13" height="22" rx="2"/>
        <circle class="icon-solid" cx="963" cy="318" r="10"/>
        <rect class="icon" x="988" y="307" width="13" height="21" rx="2"/>
        <circle class="icon" cx="994" cy="354" r="10"/>
        <path class="icon" d="M984 354 h20 M994 344 q-7 10 0 20 q7 -10 0 -20"/>
      </g>

      <text class="company-name" x="1005" y="460" text-anchor="end">FYROLT BV</text>
      <text class="contact-line" x="1005" y="525" text-anchor="end">Lindenwerf 38, 1027 HX Amsterdam</text>
    </svg>
  </div>
</body>
</html>
```